Letterhead Design Project

Professional but modern letterhead.

Target Market(s)

mining companies

Industry/Entity Type

It Professional

Colors

Designer to choose colors to be used in the design.

```html
<!DOCTYPE html>
<html lang="en">
<head>
<meta charset="utf-8">
<title>KOVA Letterhead</title>
<link rel="stylesheet" href="https://fonts.googleapis.com/css2?family=Source+Sans+3:wght@400;600&display=swap">
<style>
  :root {
    --brand-blue: #0b4890;
    --brand-blue-soft: #3361a2;
    --ink-blue: #1f3a8f;
    --paper: #ffffff;
    --canvas: #ffffff;
    --paper-edge: #d4d4d4;
    --mark-grey: #d9d9d9;
    --text-light: #e8eef8;
  }
  * { margin: 0; padding: 0; box-sizing: border-box; }
  html, body {
    width: 1200px;
    height: 767px;
    overflow: hidden;
    background: var(--canvas);
    font-family: "Source Sans 3", "Myriad Pro", Arial, sans-serif;
  }
  .sheet {
    position: absolute;
    top: 9px;
    width: 580px;
    height: 751px;
    overflow: hidden;
  }
  .sheet--back {
    left: 8px;
    background: var(--brand-blue);
  }
  .sheet--front {
    left: 610px;
    background: var(--paper);
    border: 1px solid var(--paper-edge);
  }
  .contact {
    position: absolute;
    font-size: 7.6px;
    line-height: 1;
    font-weight: 400;
  }
  .contact p { white-space: nowrap; }
  .sheet--back .contact {
    left: 19px;
    top: 28px;
    color: var(--text-light);
  }
  .sheet--back .contact p + p { margin-top: 3.8px; }
  .sheet--front .contact {
    left: 18px;
    top: 32px;
    color: var(--ink-blue);
  }
  .sheet--front .contact p + p { margin-top: 4.4px; }
  .brand-name {
    position: absolute;
    right: 26px;
    top: 56px;
    font-size: 20px;
    font-weight: 600;
    color: var(--brand-blue);
    letter-spacing: 0.5px;
    line-height: 1;
  }
  .brand-dot {
    position: absolute;
    right: 39px;
    top: 30px;
    width: 20px;
    height: 20px;
    border-radius: 50%;
    background: var(--brand-blue);
  }
  .footer-mark {
    position: absolute;
    left: 290px;
    bottom: 0;
    transform: translateX(-50%);
  }
</style>
</head>
<body>
  <section class="sheet sheet--back" aria-label="Letterhead back">
    <div class="contact">
      <p>Address Line Here 1, Address Line Here 2</p>
      <p>Tel &nbsp;: &nbsp;+001 134 1345, Fax : +001 134 1345</p>
      <p>Email : test@test.com</p>
      <p>Website :www.test.com</p>
    </div>
    <svg class="footer-mark" width="260" height="130" viewBox="0 0 260 130" aria-hidden="true">
      <circle cx="130" cy="130" r="128" fill="var(--brand-blue-soft)"/>
    </svg>
  </section>

  <section class="sheet sheet--front" aria-label="Letterhead front">
    <div class="contact">
      <p>Address Line Here 1, Address Line Here 2</p>
      <p>Tel &nbsp;: &nbsp;+001 134 1345, Fax : +001 134 1345</p>
      <p>Email : test@test.com, Website :www.test.com</p>
    </div>
    <span class="brand-dot" aria-hidden="true"></span>
    <div class="brand-name">KOVA</div>
    <svg class="footer-mark" width="260" height="130" viewBox="0 0 260 130" aria-hidden="true">
      <circle cx="130" cy="130" r="128" fill="var(--mark-grey)"/>
    </svg>
  </section>
</body>
</html>
```